Web page design for food business

The website is pantryloop.com.au and is an ordering website with thumbnails for purchasing high quality delicatessen products + fruit & vegetables.
The site is simple with a focus on clicking foods to buy and then pay for. There are no complicated product reviews or anything. Aside from the normal about us and contact us pages the website is essentially thumbnails for ordering and a high quality homepage to educate and showcase the business when people go to the URL.
There are 2 main tasks
The first task is a page design (i.e. header, footer, sides...) to carry through for all the pages in the website.
The second task is for the homepage specifically. I want a professional looking homepage with 3 large slide banners that look "elegant" and "artisan" as this is a deli website not a general grocery website. One slider should refer to "daily deliveries" and I will leave the other 2 sliders to your professional judgement. The homepage should also provide for room under the slide banner for specials/products of the month/etc and general promotional information
Target Market(s)
higher income earners, foodies, professionals, quality foods
Industry/Entity Type
Food Store
Number of Pages Required
2 page
Requirements
Must have
- Fresh quality food ready to be delivered
- Ease of ordering
- The feel of a high quality deli
Nice to have
- References to fresh fruit and vegetables for greenery and freshness
Should not have
- .

```html
<!DOCTYPE html>
<html lang="en">
<head>
<meta charset="utf-8">
<title>pantryloop.com.au – Fresh deli &amp; produce delivered</title>
<link href="https://fonts.googleapis.com/css2?family=Oswald:wght@400;500;600&family=Open+Sans:wght@400;600;700&display=swap" rel="stylesheet">
<style>
:root{
  --orange:#ec6a2c;
  --orange-dark:#d65a1f;
  --green:#6fae3b;
  --green-dark:#5a9430;
  --charcoal:#3b3b3b;
  --ink:#444;
  --muted:#8a8a8a;
  --paper:#efeeeb;
  --white:#fff;
  --line:#dedcd8;
  --star:#f2b01e;
}
*{box-sizing:border-box;margin:0;padding:0}
html,body{width:1200px;height:2172px;overflow:hidden}
body{background:var(--paper);font-family:"Open Sans",Arial,sans-serif;color:var(--ink);font-size:13px;position:relative}
.wrap{width:1000px;margin:0 auto;position:relative}
a{color:inherit;text-decoration:none}

/* top bar */
.topbar{height:32px;background:#f7f6f3;border-bottom:1px solid var(--line);font-size:10px;text-transform:uppercase;color:var(--muted)}
.topbar .wrap{display:flex;justify-content:space-between;align-items:center;height:32px}
.topbar .right{display:flex;gap:36px}

/* header */
.header{height:116px}
.header .wrap{display:flex;align-items:center;height:116px}
.brand{font-family:"Open Sans",sans-serif;font-weight:700;font-size:22px;color:var(--charcoal);display:flex;align-items:center;gap:8px;width:320px;white-space:nowrap}
.brand .dot{width:12px;height:12px;background:var(--orange);border-radius:50%;flex:none}
.info{display:flex;align-items:center;gap:10px;width:250px}
.info .ico{width:36px;height:36px;border-radius:50%;display:flex;align-items:center;justify-content:center;flex:none}
.info .ico.cart{background:var(--green)}
.info .ico.call{background:var(--orange)}
.info strong{display:block;font-size:11px;text-transform:uppercase;color:var(--charcoal)}
.info span{font-size:11px;color:var(--muted)}
.search{margin-left:auto;width:220px;height:32px;background:var(--white);border:1px solid var(--line);display:flex;align-items:center;font-size:10px;color:var(--muted)}
.search .cat{padding:0 10px;border-right:1px solid var(--line);height:100%;display:flex;align-items:center}
.search .btn{margin-left:auto;width:32px;height:100%;background:var(--green);display:flex;align-items:center;justify-content:center}

/* nav */
.nav{display:flex;height:40px;background:var(--orange)}
.nav a{font-family:"Oswald",sans-serif;font-size:13px;color:var(--white);padding:0 22px;display:flex;align-items:center;letter-spacing:.5px}
.nav a.active{background:var(--charcoal)}

/* hero */
.hero{margin-top:32px;height:500px;position:relative;background:linear-gradient(90deg,#6b8a3a 0%,#b84a2a 30%,#a86a3c 55%,#c6935f 70%,#d4a676 100%)}
.hero-copy{position:absolute;right:60px;top:150px;text-align:right;color:var(--white)}
.hero-copy h2{font-family:"Oswald",sans-serif;font-weight:600;font-size:58px;line-height:1;letter-spacing:1px}
.hero-copy p{font-size:13px;margin-top:10px;line-height:1.4}
.btn-dark{display:inline-block;background:var(--charcoal);color:var(--white);font-size:11px;font-weight:700;padding:10px 16px;margin-top:22px;text-transform:uppercase}
.hero-dots{position:absolute;right:60px;top:392px;display:flex;gap:6px}
.hero-dots span{width:16px;height:16px;border-radius:50%;background:rgba(60,60,60,.75)}

/* promos */
.promos{display:flex;gap:16px;margin-top:32px;height:208px}
.promo{flex:1;background:var(--white);position:relative;overflow:hidden}
.promo .art{position:absolute;inset:0}
.promo h3{position:absolute;font-family:"Oswald",sans-serif;font-weight:400;color:var(--charcoal)}
.promo.delivery h3{left:60px;top:22px;font-size:28px}
.promo.delivery .art{top:70px;background:linear-gradient(180deg,#fff 0%,#f4d24a 45%,#f0c238 100%)}
.promo.offer .art{right:40%;background:linear-gradient(180deg,#f6f2ea,#c9a26a 60%,#b3262a 100%)}
.promo.offer h3{right:20px;top:40px;font-size:18px}
.promo .pill{position:absolute;border:1px solid var(--orange);color:var(--orange);font-size:9px;font-weight:700;padding:4px 12px;text-transform:uppercase}
.promo.offer .pill{right:36px;top:80px}
.promo.fresh .art{right:45%;background:linear-gradient(160deg,#f7f4ec,#f2c84b 45%,#8cc04a 100%)}
.promo.fresh h3{right:20px;top:20px;text-align:right;font-size:16px;line-height:1.25}
.promo.fresh h3 b{display:block;color:var(--orange);font-weight:500;font-size:22px}
.promo.fresh .pill{right:30px;top:118px}

/* main */
.main{display:flex;gap:28px;margin-top:40px}
.products{width:760px}
.section-title{display:flex;justify-content:space-between;align-items:center;height:24px}
.section-title h2{font-family:"Oswald",sans-serif;font-weight:500;font-size:22px;color:var(--charcoal)}
.section-title .arrows{display:flex;gap:4px}
.section-title .arrows span{width:20px;height:20px;border-radius:50%;background:#c9c7c2}
.grid{display:grid;grid-template-columns:repeat(3,232px);gap:40px 32px;margin-top:20px}
.card{background:var(--white);height:348px;position:relative;text-align:center;padding-top:36px}
.card .badge{position:absolute;top:14px;left:50%;transform:translateX(-50%);width:22px;height:22px;border-radius:50%;background:var(--orange)}
.card .photo{width:150px;height:150px;border-radius:50%;margin:6px auto 0;border:6px solid #f3f2ef}
.card h4{font-size:11px;font-weight:700;text-transform:uppercase;margin-top:26px;color:var(--charcoal)}
.card p{font-size:10px;color:var(--muted);margin:8px 30px 0;line-height:1.45}
.card .meta{display:flex;justify-content:center;gap:12px;margin-top:14px;font-size:11px;align-items:center}
.card .stars{color:var(--star);letter-spacing:1px}
.card .price{color:var(--orange);font-weight:700}

.sidebar{width:212px}
.categories{background:var(--white);height:420px}
.categories h3{background:var(--green);color:var(--white);font-family:"Oswald",sans-serif;font-weight:500;font-size:15px;padding:13px 16px}
.categories ul{list-style:none;padding:14px 16px}
.categories li{font-size:11px;color:var(--ink);padding:6px 0;display:flex;gap:8px;align-items:center}
.categories li::before{content:"";width:6px;height:6px;background:var(--green);border-radius:50%}
.side-banner{margin-top:28px;height:380px;position:relative;background:linear-gradient(160deg,#8c2a22 0%,#6a4a3a 50%,#3e3a5a 100%)}
.side-banner p{position:absolute;left:16px;top:24px;font-family:"Oswald",sans-serif;font-weight:500;font-size:26px;line-height:1.15;color:var(--white);text-transform:uppercase}

/* footer */
.footer{position:absolute;left:0;top:1860px;width:1200px;height:232px;background:var(--orange);color:var(--white)}
.footer .wrap{display:flex;padding-top:36px}
.footer h5{font-family:"Oswald",sans-serif;font-weight:500;font-size:14px;text-transform:uppercase;margin-bottom:10px}
.footer .col{font-size:10px;line-height:1.7}
.footer .news{width:380px}
.footer .news p{width:300px;opacity:.9}
.footer .field{display:flex;margin-top:12px}
.footer .field span{width:200px;height:28px;background:var(--white);color:var(--muted);padding:6px 10px}
.footer .field b{background:var(--charcoal);padding:6px 12px}
.footer .links{width:210px}
.bottombar{position:absolute;left:0;top:2092px;width:1200px;height:80px;background:var(--charcoal)}
.bottombar .wrap{display:flex;align-items:center;justify-content:space-between;height:80px}
.bottombar .brand{color:var(--white);font-size:20px}
.pay{display:flex;gap:6px}
.pay span{width:32px;height:20px;background:#5a5a5a;border-radius:2px}
</style>
</head>
<body>
<div class="topbar"><div class="wrap">
  <span>Get directions</span>
  <div class="right"><span>Create an Account</span><span>My Account ▾</span><span>Currency ▾</span></div>
</div></div>

<header class="header"><div class="wrap">
  <a class="brand" href="#"><span class="dot"></span>pantryloop.com.au</a>
  <div class="info">
    <div class="ico cart"><svg width="18" height="18" viewBox="0 0 24 24" fill="none" stroke="#fff" stroke-width="2"><path d="M3 4h3l2 11h11l2-8H7"/><circle cx="9" cy="20" r="1.5"/><circle cx="18" cy="20" r="1.5"/></svg></div>
    <div><strong>Shopping cart</strong><span>0 items - $0.00</span></div>
  </div>
  <div class="info">
    <div class="ico call"><svg width="16" height="16" viewBox="0 0 24 24" fill="#fff"><path d="M6.6 10.8a15 15 0 006.6 6.6l2.2-2.2c.3-.3.7-.4 1-.2 1.1.4 2.3.6 3.6.6.6 0 1 .4 1 1V20c0 .6-.4 1-1 1A17 17 0 013 4c0-.6.4-1 1-1h3.5c.6 0 1 .4 1 1 0 1.3.2 2.5.6 3.6.1.3 0 .7-.2 1z"/></svg></div>
    <div><strong>Call toll free</strong><span>+61 2 5550 0148</span></div>
  </div>
  <div class="search"><span class="cat">All Categories ▾</span><span class="btn"><svg width="14" height="14" viewBox="0 0 24 24" fill="none" stroke="#fff" stroke-width="3"><circle cx="10" cy="10" r="6"/><path d="M15 15l6 6"/></svg></span></div>
</div></header>

<div class="wrap">
  <nav class="nav">
    <a class="active" href="#">HOME</a><a href="#">SPECIALS</a><a href="#">OUR PRODUCTS</a><a href="#">FRESH FRUITS</a><a href="#">DELI DELIVERY</a><a href="#">BLOG</a><a href="#">CONTACT US</a>
  </nav>

  <section class="hero" role="img" aria-label="Fresh vegetables, tomatoes and herbs spread across a rustic wooden board">
    <div class="hero-copy">
      <h2>DAILY<br>DELIVERIES</h2>
      <p>Fine deli goods and fresh produce, brought<br>straight to your door every morning</p>
      <span class="btn-dark">Shop now ›</span>
    </div>
    <div class="hero-dots"><span></span><span></span></div>
  </section>

  <section class="promos">
    <div class="promo delivery">
      <div class="art" role="img" aria-label="Yellow delivery van illustration"></div>
      <h3>FREE DELIVERY</h3>
    </div>
    <div class="promo offer">
      <div class="art" role="img" aria-label="Wicker basket filled with strawberries"></div>
      <h3>PROMOTIONAL</h3>
      <span class="pill">Shop now</span>
    </div>
    <div class="promo fresh">
      <div class="art" role="img" aria-label="Lemons, limes and fresh greens"></div>
      <h3>FRESH <b>FRUITS &amp;<br>VEGETABLES</b></h3>
      <span class="pill">Shop now</span>
    </div>
  </section>

  <div class="main">
    <section class="products">
      <div class="section-title"><h2>SPECIALS &amp; PRODUCTS</h2><div class="arrows"><span></span><span></span></div></div>
      <div class="grid">
        <article class="card"><span class="badge"></span><div class="photo" role="img" aria-label="Strawberries" style="background:radial-gradient(circle,#e23a3a,#b3202a 60%,#fff 62%)"></div><h4>Strawberry</h4><p>Sweet ripe berries picked fresh for your table</p><div class="meta"><span class="stars">★★★☆☆</span><span class="price">$15.00</span></div></article>
        <article class="card"><span class="badge"></span><div class="photo" role="img" aria-label="Mixed fresh fruit" style="background:radial-gradient(circle,#d44a3a,#8fb44a 60%,#fff 62%)"></div><h4>Nam nec tellus</h4><p>Seasonal fruit selection packed with care daily</p><div class="meta"><span class="stars">★★★☆☆</span><span class="price">$15.00</span></div></article>
        <article class="card"><span class="badge"></span><div class="photo" role="img" aria-label="Broccoli" style="background:radial-gradient(circle,#6aa23a,#3f7a26 60%,#fff 62%)"></div><h4>Broccoli</h4><p>Crisp green florets grown by local farmers</p><div class="meta"><span class="stars">★★★☆☆</span><span class="price">$15.00</span></div></article>
        <article class="card"><span class="badge"></span><div class="photo" role="img" aria-label="Tomatoes" style="background:radial-gradient(circle,#e0442e,#b52a1e 60%,#fff 62%)"></div><h4>Tomatoes</h4><p>Vine ripened and full of rich summer flavour</p><div class="meta"><span class="stars">★★★☆☆</span><span class="price">$15.00</span></div></article>
        <article class="card"><span class="badge"></span><div class="photo" role="img" aria-label="Bananas" style="background:radial-gradient(circle,#f7d640,#e8b820 60%,#fff 62%)"></div><h4>Banana</h4><p>Golden bananas perfect for breakfast or baking</p><div class="meta"><span class="stars">★★★☆☆</span><span class="price">$15.00</span></div></article>
        <article class="card"><span class="badge"></span><div class="photo" role="img" aria-label="Bilberries" style="background:radial-gradient(circle,#4a3a7a,#22204a 60%,#fff 62%)"></div><h4>Bilberry</h4><p>Small dark berries bursting with natural taste</p><div class="meta"><span class="stars">★★★☆☆</span><span class="price">$15.00</span></div></article>
      </div>
    </section>

    <aside class="sidebar">
      <div class="categories">
        <h3>CATEGORIES</h3>
        <ul>
          <li>Cheeses (8)</li><li>Confectionery (6)</li><li>Dips, Spreads (4)</li><li>Fresh Fruit (12)</li><li>Fruit (7)</li><li>Herbs (5)</li><li>Nuts &amp; Seeds (9)</li><li>Milk &amp; Eggs (6)</li><li>Olives &amp; Pickles (4)</li><li>Pantry (3)</li><li>Salt &amp; Seasonings (5)</li>
        </ul>
      </div>
      <div class="side-banner" role="img" aria-label="Strawberries and blueberries close up">
        <p>Fresh<br>quality<br>food<br>ready<br>to be<br>delivered</p>
      </div>
    </aside>
  </div>
</div>

<footer class="footer"><div class="wrap">
  <div class="col news">
    <h5>Newsletter</h5>
    <p>Sign up for seasonal specials, new deli arrivals and weekly recipe ideas from our kitchen.</p>
    <div class="field"><span>Enter your email here</span><b>Sign Up</b></div>
  </div>
  <div class="col links"><h5>Information</h5>About Us<br>Products<br>Fresh Fruits<br>Free Delivery<br>Contact Us</div>
  <div class="col links"><h5>Customer Service</h5>Contact Us<br>Returns<br>Site Map<br>Gift Vouchers</div>
  <div class="col"><h5>Contact Information</h5>12 Market Lane, Sydney NSW<br>+61 2 5550 0148<br>hello@pantryloop.com.au</div>
</div></footer>

<div class="bottombar"><div class="wrap">
  <span class="brand"><span class="dot"></span>pantryloop.com.au</span>
  <div class="pay"><span></span><span></span><span></span><span></span></div>
</div></div>
</body>
</html>
```